The Harbor Parking Lot Vision Flags

Size: 3 banners - 2' x 4' banners (portrait)
Design: all the same design with different text
text on banner 1: Building Solid Lives
text on banner 2: Come. Hear. Do. Luke 6
text on banner 3: Worship Center
Details: Use the colors red, white and black and use the h logo attached
Make white the main color (not too much black and not too much red) Keep design simple - not a lot of different textures - more "quince like"

Target Market(s)

30-50 year olds

Industry/Entity Type

Parking

Font styles to use
Sans Serif

Colors
ec1f27
fbfbfb
1b1b1b

Requirements
Must have
• Logo and the colors red white and black
Nice to have
• simple - clean - cool
Should not have
• busy backgrounds and textures

```html
<!DOCTYPE html>
<html lang="en">
<head>
<meta charset="utf-8">
<title>The Harbor Parking Lot Vision Flags</title>
<link rel="stylesheet" href="https://fonts.googleapis.com/css2?family=Arimo:wght@400;700&display=swap">
<style>
  :root {
    --harbor-red: #ec1f27;
    --flag-white: #fbfbfb;
    --ink-black: #1b1b1b;
    --backdrop: #ececec;
  }
  * { box-sizing: border-box; margin: 0; padding: 0; }
  html, body {
    width: 1200px;
    height: 849px;
    overflow: hidden;
    background: var(--backdrop);
    font-family: "Arimo", Helvetica, Arial, sans-serif;
  }
  .flag-set { position: relative; width: 1200px; height: 849px; }
  .flag {
    position: absolute;
    top: 118px;
    width: 306px;
    height: 613px;
    background: var(--flag-white);
  }
  .flag--building { left: 87px; }
  .flag--come { left: 444px; }
  .flag--worship { left: 809px; }
  .flag__corners { position: absolute; inset: 0; width: 100%; height: 100%; }
  .flag__corners polygon { fill: var(--harbor-red); }
  .flag__brand {
    position: absolute;
    left: 14px;
    top: 24px;
    color: var(--flag-white);
    font-weight: 700;
    font-size: 15px;
    letter-spacing: 0.2px;
    line-height: 1;
  }
  .flag__frame {
    position: absolute;
    left: 31px;
    top: 195px;
    width: 245px;
    height: 224px;
    border: 3.5px solid var(--ink-black);
    display: flex;
    flex-direction: column;
    justify-content: center;
    align-items: center;
    color: var(--ink-black);
    font-weight: 700;
    text-transform: uppercase;
    line-height: 0.95;
    text-align: center;
  }
  .slogan--building .slogan__lead { font-size: 35px; letter-spacing: 0.3px; }
  .slogan--building .slogan__big { font-size: 64px; letter-spacing: -1.5px; }
  .slogan--come { align-items: flex-start; padding-left: 48px; }
  .slogan--come .slogan__line { font-size: 45px; letter-spacing: -0.5px; }
  .slogan__do {
    display: flex;
    align-items: flex-end;
    font-size: 72px;
    letter-spacing: -2px;
    line-height: 0.8;
    margin-top: 4px;
  }
  .slogan__verse {
    width: 54px;
    height: 54px;
    border-radius: 50%;
    background: var(--ink-black);
    color: var(--flag-white);
    font-weight: 400;
    font-size: 12px;
    letter-spacing: 0;
    display: flex;
    align-items: center;
    justify-content: center;
    margin-left: -6px;
  }
  .slogan__dot {
    width: 11px;
    height: 11px;
    background: var(--ink-black);
    margin-left: 2px;
  }
  .slogan--worship .slogan__line { font-size: 44px; letter-spacing: -0.3px; line-height: 1.05; }
</style>
</head>
<body>
<main class="flag-set">
  <section class="flag flag--building">
    <svg class="flag__corners" viewBox="0 0 306 613" aria-hidden="true">
      <polygon points="0,0 161,0 0,194"/>
      <polygon points="306,541 306,613 247,613"/>
    </svg>
    <span class="flag__brand">The Harbor</span>
    <div class="flag__frame slogan--building">
      <span class="slogan__lead">Building</span>
      <span class="slogan__big">Solid</span>
      <span class="slogan__big">Lives</span>
    </div>
  </section>

  <section class="flag flag--come">
    <svg class="flag__corners" viewBox="0 0 306 613" aria-hidden="true">
      <polygon points="0,0 161,0 0,194"/>
      <polygon points="306,541 306,613 247,613"/>
    </svg>
    <span class="flag__brand">The Harbor</span>
    <div class="flag__frame slogan--come">
      <span class="slogan__line">Come.</span>
      <span class="slogan__line">Here.</span>
      <span class="slogan__do">D<span class="slogan__verse">LUKE 6</span><span class="slogan__dot"></span></span>
    </div>
  </section>

  <section class="flag flag--worship">
    <svg class="flag__corners" viewBox="0 0 306 613" aria-hidden="true">
      <polygon points="0,0 161,0 0,194"/>
      <polygon points="306,541 306,613 247,613"/>
    </svg>
    <span class="flag__brand">The Harbor</span>
    <div class="flag__frame slogan--worship">
      <span class="slogan__line">Worship</span>
      <span class="slogan__line">Centre</span>
    </div>
  </section>
</main>
</body>
</html>
```